Web Design Project (Mente Lumo)

We are going to do a therapy template to a psychologist. The site already exists, adress: www.mentelumo.net. So, its a total redesign job. I'm from Brazil, the language is PT-BR, so I'm gonna translate what you think be necessary. You can use the current structure from the website as a base to the new design. Check this template to see what I usually like: http://www.layoutkiosk.example/demo/51937.html
Updates

I'm waiting for new creative designs. The 'structure' image is just for 'pb'.

Requirements
Must have
• We need a modern menu, it should use a cool font style and make some kind of effect and little noise when the user pass over with the mouse (FLASH/HTML 5). The main page must emphasize the fact that we offer online treatment, like a picture or frame saying "Online Treatment, click here". It must also show the therapist picture and her name. The colors need to pass a tranquility feeling. The clinic telephone must always be present, doesn't matter which page the user is. The website must adapt to any resolution above 1024x768, crossbrowsing and accept javascript (I'll use www.agendrix.example, so its necessary embed code)
Nice to have
• I would appreciate if there was some kind of slow background animation, passing behind the text using the transparency.
Should not have
• Can't take too long to load, and won't have news or blog

```html
<!DOCTYPE html>
<html lang="pt-BR">
<head>
<meta charset="utf-8">
<title>Mente Lumo</title>
<link rel="stylesheet" href="https://fonts.googleapis.com/css2?family=Arimo:wght@400;700&display=swap">
<style>
:root{
  --nav-top:#75a3d6;
  --nav-bottom:#3e70b1;
  --nav-divider:#2f5c96;
  --panel:#3b414d;
  --panel-dark:#343a45;
  --panel-line:#2a2f38;
  --accent-green:#7cb82c;
  --accent-green-dark:#5f9a1c;
  --heading-blue:#3f78ba;
  --text:#4a4a4a;
  --text-dark:#222;
  --rule:#e2e2e2;
  --btn-top:#6d9ad0;
  --btn-bottom:#3f72b2;
  --footer-top:#43658f;
  --footer-bottom:#2c4b72;
  --white:#fff;
}
*{margin:0;padding:0;box-sizing:border-box}
html,body{width:1067px;height:1200px;overflow:hidden;background:var(--white)}
body{font-family:"Arimo",Arial,sans-serif;color:var(--text);position:relative}
.page{position:absolute;left:42px;top:0;width:983px;height:1200px}

.main-nav{position:absolute;left:0;top:0;width:983px;height:63px;display:flex;background:linear-gradient(var(--nav-top),var(--nav-bottom))}
.main-nav a{display:flex;align-items:center;justify-content:center;color:var(--white);font-weight:700;font-size:16px;text-decoration:none;border-right:1px solid var(--nav-divider);text-shadow:0 1px 2px rgba(0,0,0,.45)}
.main-nav a:last-child{border-right:0}

.hero{position:absolute;left:0;top:63px;width:983px;height:523px}
.hero-photo{position:absolute;left:370px;top:0;width:613px;height:523px;background:linear-gradient(100deg,#c9475c 0%,#d8a58e 35%,#e9e3da 55%,#5c6f8f 80%,#c9b59a 100%)}
.hero-panel{position:absolute;left:0;top:0;width:370px;height:523px;background:linear-gradient(var(--panel),var(--panel-dark))}
.contact-bar{height:63px;border-bottom:1px solid var(--panel-line);display:flex;align-items:center;padding-left:32px;gap:38px;color:#e6e6e6;font-weight:700;font-size:14px}
.contact-bar span{display:flex;align-items:center;gap:6px}
.brand{height:118px;border-bottom:1px solid var(--panel-line);display:flex;align-items:center;justify-content:center;gap:10px;color:#dfe6ec;font-size:28px;font-weight:700}
.brand-dot{width:14px;height:14px;border-radius:50%;background:#8fc5c9}
.hero-title{position:absolute;left:33px;top:217px;color:var(--white);font-size:27px;font-weight:400}
.hero-title strong{font-size:31px;font-weight:700;margin-left:4px}
.hero-text{position:absolute;left:33px;top:278px;width:260px;color:#f1f1f1;font-size:14.5px;line-height:21px}
.btn-green{position:absolute;left:33px;top:451px;width:156px;height:32px;background:linear-gradient(var(--accent-green),var(--accent-green-dark));color:var(--white);font-size:20px;font-weight:700;display:flex;align-items:center;justify-content:center;text-shadow:0 1px 2px rgba(0,0,0,.4)}

.section-rule{position:absolute;left:0;top:617px;width:983px;height:1px;background:var(--rule)}
.v-rule{position:absolute;width:1px;background:var(--rule)}
.h-rule{position:absolute;height:1px;background:var(--rule)}

.teaser{position:absolute;width:240px}
.teaser h2,.profile h2,.topics h2{color:var(--heading-blue);font-size:17.5px;font-weight:700}
.teaser p{margin-top:10px;font-size:14px;line-height:20px;padding-left:1px}
.btn-blue{display:inline-flex;align-items:center;justify-content:center;width:104px;height:21px;background:linear-gradient(var(--btn-top),var(--btn-bottom));color:var(--white);font-size:13.5px;font-weight:700;text-shadow:0 1px 1px rgba(0,0,0,.35)}
.teaser .btn-blue{margin-top:13px}

.profile-photo{position:absolute;left:28px;top:860px;width:126px;height:154px;background:linear-gradient(#6d6d6d,#bdbdbd 60%,#e9e9e9)}
.profile{position:absolute;left:182px;top:858px;width:400px}
.profile h3{font-size:14.5px;font-weight:400;color:var(--text-dark);margin-top:3px}
.profile p{margin-top:22px;font-size:14px;line-height:20px;padding-left:2px}
.profile .btn-blue{margin-top:21px;margin-left:2px}

.topics{position:absolute;left:629px;top:651px;width:340px}
.topic-list{list-style:none;display:grid;grid-template-columns:143px 180px;grid-auto-flow:column;grid-template-rows:repeat(12,28.2px);margin-top:23px;padding-left:11px}
.topic-list li{font-size:13.5px;display:flex;align-items:center;gap:10px}
.topic-list li::before{content:"";width:11px;height:11px;border-radius:50%;background:radial-gradient(circle at 35% 35%,#fff,#aaa);border:1px solid #999}

.site-footer{position:absolute;left:0;top:1054px;width:983px;height:146px;background:linear-gradient(var(--footer-top),var(--footer-bottom));color:var(--white);font-size:11.5px;line-height:14.5px;text-align:center;padding-top:47px}
</style>
</head>
<body>
<div class="page">
  <nav class="main-nav">
    <a style="width:104px">Home</a>
    <a style="width:201px">Atendimento Online</a>
    <a style="width:145px">Tratamentos</a>
    <a style="width:129px">Perguntas</a>
    <a style="width:141px">Consultório</a>
    <a style="width:141px">Localização</a>
    <a style="width:122px">Contato</a>
  </nav>

  <section class="hero">
    <div class="hero-photo" role="img" aria-label="Foto de uma mulher sorridente deitada em um sofá claro"></div>
    <div class="hero-panel">
      <div class="contact-bar">
        <span><svg width="26" height="20" viewBox="0 0 26 20"><path d="M2 7c3-5 19-5 22 0l-1 3-5-1v-2c-3-1-7-1-10 0v2l-5 1z" fill="#e6e6e6"/><rect x="6" y="11" width="14" height="8" rx="2" fill="#e6e6e6"/><circle cx="13" cy="15" r="2.3" fill="#3b414d"/></svg>(11) 4050-7731</span>
        <span><svg width="16" height="24" viewBox="0 0 16 24"><rect x="1" y="1" width="14" height="22" rx="2" fill="#e6e6e6"/><rect x="3" y="3" width="10" height="7" fill="#3b414d"/><g fill="#3b414d"><rect x="3" y="12" width="2.5" height="2"/><rect x="7" y="12" width="2.5" height="2"/><rect x="11" y="12" width="2.5" height="2"/><rect x="3" y="16" width="2.5" height="2"/><rect x="7" y="16" width="2.5" height="2"/><rect x="11" y="16" width="2.5" height="2"/></g></svg>(11) 9080-4457</span>
      </div>
      <div class="brand"><span class="brand-dot"></span>Mente Lumo</div>
      <h1 class="hero-title">Partiendo <strong>PRINCIPES</strong></h1>
      <p class="hero-text">Solet iuvaret iudicabit nec ea, ne has enim propriae. Ex nec mazim imperdiet, decore nullam repudiandae ut ius. Elitr tation quo et, no cum odio agam munere. No cum aeque aperiam, facer ponderum explicari</p>
      <a class="btn-green">Read more</a>
    </div>
  </section>

  <div class="section-rule"></div>
  <div class="v-rule" style="left:291px;top:641px;height:157px"></div>
  <div class="v-rule" style="left:600px;top:641px;height:381px"></div>
  <div class="h-rule" style="left:27px;top:821px;width:549px"></div>

  <article class="teaser" style="left:26px;top:651px">
    <h2>Mel ei sapientem</h2>
    <p>Solet iuvaret iudicabit nec ea, ne has enim propriae. Ex nec mazim imperdiet, decore nullam</p>
    <a class="btn-blue">Read more</a>
  </article>
  <article class="teaser" style="left:340px;top:651px">
    <h2>Mel ei sapientem</h2>
    <p>Solet iuvaret iudicabit nec ea, ne has enim propriae. Ex nec mazim imperdiet, decore nullam</p>
    <a class="btn-blue">Read more</a>
  </article>

  <div class="profile-photo" role="img" aria-label="Retrato em preto e branco da terapeuta"></div>
  <article class="profile">
    <h2>Mel ei sapientem moderatius deterruisset</h2>
    <h3>CU UBIQUE ERIPUIT ATOMORUM EOS</h3>
    <p>Solet iuvaret iudicabit nec ea, ne has enim propriae. Ex nec mazim imperdiet, decore nullam repudiandae ut ius.</p>
    <a class="btn-blue">Read more</a>
  </article>

  <section class="topics">
    <h2>Mel ei sapientem moderatius</h2>
    <ul class="topic-list">
      <li>Reformidans</li><li>Iuvaret</li><li>Consequuntur</li><li>Ullamcorper</li><li>Essent</li><li>Gloriatur</li><li>Dicam</li><li>Primis</li><li>Scriptorem</li><li>Nulla</li><li>Dolore</li><li>Aliquando</li>
      <li>Reformidans Iuvaret</li><li>Consequuntur</li><li>Ullamcorper Essent</li><li>Gloriatur Dicam</li><li>Primis Scriptorem</li><li>Nulla Dolore Aliquando</li><li>Reformidans Iuvaret</li><li>Consequuntur</li><li>Ullamcorper Essent</li><li>Gloriatur Dicam</li><li>Primis Scriptorem</li><li>Nulla Dolore Aliquando</li>
    </ul>
  </section>

  <footer class="site-footer">
    Solet iuvaret iudicabit nec ea, ne has enim propriae.<br>
    Ex nec mazim imperdiet, decore nullam repudiandae ut ius. Elitr tation quo et, no cum odio<br>
    agam munere.
  </footer>
</div>
</body>
</html>
```